Ridgeway Teen Circle (Flyer)

I want a flyer to advertise my service.
Details below, and logo's to use are attached.

A girls only after school program, 11-14yrs, as OSHC is no longer avail, dedicated to coaching & mentoring our girls into strong, independent young women.

The Brainchild of Rebecca Tolland, Ridgeway Teen Circle was created to address the growing demand for after school/school holiday supervision for kids moving from primary into high school, when OSHC ceases to exist.
With over 12 years experience mentoring and coaching young women in the corporate world, Bec decided to leave her role as a Director with Corlana Bank, and follow her passion.
Bec, along with her sister Jocelyn, who has over 10 years experience in local communities as a Youth Worker, and is also a qualified Enrolled Nurse, embarked on building a program designed to keep parents happy (by knowing their girls are safe) and dedicated to coaching and mentoring our girls into strong, independent young women.
Open every afternoon and during school holidays, we look to offer;
- Daily meditation
- Healthy snacks
- Dedicated homework time
- Organised group activity, led by qualified instructors (yoga, fitness class, soccer etc)
- Regular guests speakers, addressing issues/concerns for young people today
- SOCIAL MEDIA FREE ZONE

Located 317 Pembury Rd, Baulkham Hills (across from Ardmore Private Hospital)
Open 3-6pm Monday to Friday

Facebook page: http://ridgewayteencircle.example/community
Email: info@ridgewayteencircle.example.com.au
Mobile: 0400555183

Target Market(s)

Parents of teenage girls, teenage girls 11-14 years

Industry/Entity Type

School

Font styles to use
Sans Serif

Colors
b768aa
e667a6

Requirements
Must have
• What progam is - see brief
• Who runs it
Should not have
• Not be too busy, not overly mature images

```html
<!DOCTYPE html>
<html lang="en">
<head>
<meta charset="utf-8">
<title>Ridgeway Teen Circle – After School Program</title>
<link href="https://fonts.googleapis.com/css2?family=Cinzel:wght@700&family=Courier+Prime:wght@700&family=Hind:wght@400;600&family=Montserrat:wght@700&family=Roboto+Condensed:wght@400&display=swap" rel="stylesheet">
<style>
  :root {
    --pink: #f24ff0;
    --pink-bright: #e667e0;
    --purple: #b955f2;
    --purple-soft: #b768e8;
    --ink: #1d1630;
    --navy: #2a2d4a;
    --white: #ffffff;
    --photo-a: #3f8f6a;
    --photo-b: #c8614f;
    --photo-c: #5b6fd0;
  }
  * { box-sizing: border-box; margin: 0; padding: 0; }
  html, body { width: 934px; height: 1200px; overflow: hidden; background: var(--white); }
  .flyer { position: relative; width: 934px; height: 1200px; overflow: hidden; background: var(--white); font-family: "Hind", sans-serif; color: var(--ink); }

  .top-band { position: absolute; left: 0; top: 0; width: 934px; height: 144px; background: var(--pink); }
  .hero-photo { position: absolute; left: 0; top: 144px; width: 934px; height: 482px;
    background: linear-gradient(135deg, var(--photo-c) 0%, var(--photo-a) 35%, var(--photo-b) 65%, var(--photo-a) 100%); opacity: .85; }

  .brand-box { position: absolute; left: 628px; top: 46px; width: 268px; height: 320px; background: var(--white);
    display: flex; align-items: center; justify-content: center; gap: 10px; padding: 20px; }
  .brand-dot { width: 18px; height: 18px; border-radius: 50%; background: var(--pink); flex: none; }
  .brand-name { font-family: "Montserrat", sans-serif; font-weight: 700; font-size: 30px; line-height: 1.15; color: var(--pink); }

  .tag { position: absolute; background: var(--pink); font-family: "Cinzel", serif; font-weight: 700; color: var(--ink);
    display: flex; align-items: center; justify-content: center; font-size: 37px; letter-spacing: .3px; white-space: nowrap; }
  .tag-1 { left: 83px; top: 242px; width: 401px; height: 58px; }
  .tag-2 { left: 44px; top: 308px; width: 498px; height: 58px; }
  .tag-3 { left: 118px; top: 372px; width: 328px; height: 58px; }
  .tag-note { position: absolute; left: 112px; top: 432px; font-family: "Hind", sans-serif; font-weight: 600; font-size: 20px; color: var(--ink); }

  .mission-band { position: absolute; left: 0; top: 626px; width: 934px; height: 180px; background: var(--purple); text-align: center; }
  .mission-lead { position: absolute; left: 0; right: 0; top: 18px; font-family: "Cinzel", serif; font-weight: 700; font-size: 23px; color: var(--ink); }
  .mission-name { position: absolute; left: 0; right: 0; top: 50px; font-family: "Cinzel", serif; font-weight: 700; font-size: 38px; color: var(--ink); letter-spacing: 1.5px; }
  .mission-line { position: absolute; left: 0; right: 0; font-family: "Courier Prime", monospace; font-weight: 700; font-size: 30px;
    color: var(--white); letter-spacing: 2px; font-variant: small-caps; white-space: nowrap; }
  .mission-line-1 { top: 94px; }
  .mission-line-2 { top: 136px; }

  .section-title { position: absolute; font-family: "Montserrat", sans-serif; font-weight: 700; font-size: 24px; color: var(--navy);
    padding-left: 30px; border-left: 4px solid var(--purple-soft); line-height: 32px; }
  .who-title { left: 50px; top: 838px; }
  .offer-title { left: 604px; top: 830px; }

  .who-text { position: absolute; left: 42px; top: 900px; width: 530px; font-size: 19px; line-height: 30px; }
  .open-line { position: absolute; left: 0; width: 590px; top: 1028px; text-align: center; font-family: "Hind", sans-serif; font-weight: 600; font-size: 27px; color: var(--pink-bright); white-space: nowrap; }
  .hours-line { position: absolute; left: 12px; width: 570px; top: 1070px; text-align: center; font-family: "Cinzel", serif; font-weight: 700; font-size: 23px; color: var(--ink); }

  .offer-list { position: absolute; left: 610px; top: 874px; width: 324px; list-style: none; font-size: 20px; line-height: 31px; }
  .offer-list li { position: relative; padding-left: 30px; }
  .offer-list li::before { content: ""; position: absolute; left: 0; top: 11px; width: 8px; height: 8px; border-radius: 50%; background: var(--pink); }
  .offer-list .sub { display: block; padding-left: 8px; margin-bottom: 4px; }

  .footer { position: absolute; left: 0; top: 1112px; width: 934px; height: 88px; background: var(--purple-soft); color: var(--white);
    font-family: "Roboto Condensed", sans-serif; }
  .footer svg { position: absolute; }
  .address { position: absolute; left: 95px; top: 22px; font-size: 20px; }
  .address small { display: block; font-size: 13px; text-align: center; margin-top: 2px; }
  .phone { position: absolute; left: 440px; top: 22px; font-size: 21px; }
  .contact { position: absolute; right: 28px; top: 8px; text-align: right; font-size: 18px; line-height: 28px; }
  .social-dot { display: inline-block; width: 14px; height: 14px; background: var(--white); border-radius: 3px; vertical-align: -1px; margin-left: 6px; }
</style>
</head>
<body>
<main class="flyer">
  <div class="top-band"></div>
  <div class="hero-photo" role="img" aria-label="Flat-lay photo of red sneakers, notebooks, pencils and a red backpack on a woven green mat"></div>

  <div class="brand-box"><span class="brand-dot"></span><span class="brand-name">Ridgeway Teen Circle</span></div>

  <div class="tag tag-1">A Girls Only</div>
  <div class="tag tag-2">After School Program</div>
  <div class="tag tag-3">For 11-14yrs</div>
  <p class="tag-note">as OSHC is no longer available</p>

  <section class="mission-band">
    <p class="mission-lead">The Brainchild of Rebecca Tolland</p>
    <h1 class="mission-name">Ridgeway Teen Circle</h1>
    <p class="mission-line mission-line-1">Dedicated to Coaching &amp; Mentoring Our Girls</p>
    <p class="mission-line mission-line-2">into Strong, Independent Young women</p>
  </section>

  <h2 class="section-title who-title">WHO WE ARE</h2>
  <p class="who-text">The Brainchild of Rebecca Tolland, Ridgeway Teen Circle was created to address the growing demand for after school/school holiday supervision for kids moving from primary into high school, when OSHC ceases to exist.</p>
  <p class="open-line">Open every afternoon &amp; during school holidays</p>
  <p class="hours-line">3-6pm Monday to Friday</p>

  <h2 class="section-title offer-title">WHAT WE OFFER</h2>
  <ul class="offer-list">
    <li>Daily meditation</li>
    <li>Healthy snacks</li>
    <li>Organised group activity, <span class="sub">(yoga, fitness class, soccer etc.)</span></li>
    <li>Regular guests speakers</li>
    <li>Dedicated homework time</li>
    <li>Social media free zone</li>
  </ul>

  <footer class="footer">
    <svg style="left:62px;top:20px" width="22" height="28" viewBox="0 0 22 28" aria-hidden="true">
      <path d="M11 26 C4 17 2 13 2 10 A9 9 0 0 1 20 10 C20 13 18 17 11 26 Z" fill="none" stroke="#fff" stroke-width="1.6"/>
      <circle cx="11" cy="10" r="3.2" fill="none" stroke="#fff" stroke-width="1.6"/>
    </svg>
    <p class="address">317 Pembury Rd, Baulkham Hills<small>(across from Ardmore Private Hospital)</small></p>

    <svg style="left:398px;top:22px" width="30" height="28" viewBox="0 0 30 28" aria-hidden="true">
      <path d="M5 4 l5 -1 l3 7 l-3 2 c2 4 4 6 8 8 l2 -3 l7 3 l-1 5 c-12 1 -22 -9 -21 -21 z" fill="none" stroke="#fff" stroke-width="1.6" stroke-linejoin="round"/>
    </svg>
    <p class="phone">Call: 0400555183</p>

    <div class="contact">
      <p>e-Mail us
        <svg width="22" height="16" viewBox="0 0 22 16" aria-hidden="true" style="position:static;vertical-align:-2px;margin-left:4px">
          <rect x="1" y="1" width="20" height="14" fill="none" stroke="#fff" stroke-width="1.5"/>
          <path d="M1 1 L11 9 L21 1" fill="none" stroke="#fff" stroke-width="1.5"/>
        </svg>
      </p>
      <p>info@ridgewayteencircle.example.com.au</p>
      <p>http://ridgewayteencircle.example/community<span class="social-dot"></span></p>
    </div>
  </footer>
</main>
</body>
</html>
```